Business Card Design Project For Moving Company

Hello,

We need the business card to be 2 sided and we were thinking to use the logo on the front of the card (see file 1 attached) and the text "logo" (see file 2 attached) in the back of the card. We're looking for a powerful design that will help us build our brand, as our company is new.
We are a full service moving company (no storage) located in San Diego, CA, USA. The design should communicate to our potential customers that we have the highest level of service, customer satisfaction is our number one goal, our team is professional and efficient.

Thank you,

Dorn
Updates

Project Deadline Extended
Reason: We would like to have more time to provide feedback for the designs already submitted. Thank you, Dorn

Industry/Entity Type

Moving Company

Requirements
Must have
• Front of the card must have the following text and logo:
Haulbright, Inc
Residential And Commercial
Local And Long Distance
Address: 7312 Quillmont Rd, #146,
San Diego, CA, 92784
P: 855-372-LIFT (5438)
F: 858-529-4407
info@haul-bright.com
www.haul-bright.com

Back of the card must have the following text and text "logo" (file 2 attached):

The best compliment we can ever receive is a referral from our clients.

```html
<!DOCTYPE html>
<html lang="en">
<head>
<meta charset="utf-8">
<title>Haulbright, Inc – Business Card</title>
<link rel="stylesheet" href="https://fonts.googleapis.com/css2?family=Arimo:wght@700&display=swap">
<style>
  :root {
    --backdrop: #e4e6e9;
    --card-navy: #16254a;
    --accent-red: #e0231c;
    --ink-white: #ffffff;
    --ink-soft: #dfe4ef;
    --card-shadow: rgba(20, 28, 45, 0.28);
  }

  * { box-sizing: border-box; margin: 0; padding: 0; }

  html, body {
    width: 1200px;
    height: 893px;
    overflow: hidden;
    background: var(--backdrop);
  }

  .sheet {
    position: relative;
    width: 1200px;
    height: 893px;
    display: flex;
    flex-direction: column;
    align-items: center;
    justify-content: center;
    gap: 48px;
  }

  .card {
    position: relative;
    width: 630px;
    height: 370px;
    background: var(--card-navy);
    box-shadow: 0 10px 24px var(--card-shadow);
    overflow: hidden;
    font-family: "Arimo", Arial, sans-serif;
    font-weight: 700;
    color: var(--ink-white);
  }

  .card__band {
    position: absolute;
    left: 0;
    right: 0;
    bottom: 0;
    height: 14px;
    background: var(--accent-red);
  }

  /* Back side: brand mark and referral line */
  .card--back {
    display: flex;
    flex-direction: column;
    align-items: center;
    justify-content: center;
    gap: 34px;
    padding: 0 70px 14px;
    text-align: center;
  }

  .brand-mark {
    display: flex;
    align-items: center;
    gap: 14px;
  }

  .brand-mark__square {
    width: 34px;
    height: 34px;
    background: var(--accent-red);
  }

  .brand-mark__name {
    font-size: 40px;
    letter-spacing: 1px;
    color: var(--ink-white);
    text-transform: uppercase;
  }

  .back__tagline {
    font-size: 19px;
    line-height: 1.35;
    color: var(--ink-soft);
  }

  /* Front side: details */
  .card--front {
    display: flex;
    flex-direction: column;
    align-items: center;
    padding-top: 36px;
    text-align: center;
  }

  .front__name {
    font-size: 52px;
    line-height: 1;
    letter-spacing: 0.5px;
    text-transform: uppercase;
    color: var(--ink-white);
  }

  .front__services {
    margin-top: 14px;
    font-size: 21px;
    line-height: 1.12;
  }

  .front__services .divider {
    display: inline-block;
    width: 7px;
    height: 7px;
    margin: 0 6px 4px;
    background: var(--ink-white);
    transform: rotate(45deg);
  }

  .front__contact {
    margin-top: 20px;
    font-size: 16px;
    line-height: 1.2;
    font-style: normal;
  }

  .front__contact .label { display: block; }
</style>
</head>
<body>
  <main class="sheet">
    <section class="card card--back" aria-label="Card back">
      <div class="brand-mark">
        <span class="brand-mark__square" aria-hidden="true"></span>
        <span class="brand-mark__name">Haulbright</span>
      </div>
      <p class="back__tagline">The best compliment we can ever receive<br>is a referral from our clients.</p>
      <div class="card__band"></div>
    </section>

    <section class="card card--front" aria-label="Card front">
      <h1 class="front__name">Haulbright</h1>
      <p class="front__services">
        Residential<span class="divider" aria-hidden="true"></span>Commercial<br>
        Local<span class="divider" aria-hidden="true"></span>Long Distance
      </p>
      <address class="front__contact">
        <span class="label">Address:</span>
        7312 Quillmont Rd, #146,<br>
        San Diego, CA, 92784<br>
        P: 855-372-LIFT (5438)<br>
        F: 858-529-4407<br>
        info@haul-bright.com<br>
        www.haul-bright.com
      </address>
      <div class="card__band"></div>
    </section>
  </main>
</body>
</html>
```